Bubble solution bottle label for children

I would like a design for a label for a new bubble solution we have created. We'd like it to appeal to parents as well as 5-10 year old kids. It needs to be whimsical and attractive. The name of the bubbles is:

Plimmo Fizzles!

We also need a portion of the label to include the following warning:
"Do not drink bubble solution. If swallowed drink lots of water. Bubble solution is not intended for human or animal consumption. If it comes in contact with your eyes, rinse immediately with water"

The label is full bleed and needs to meet the criteria below:
Horizontal
3.54" x 2.05"
90 x 52 mm
1063 x 615 pixels

Target Market(s)

5-10 years old children and their parents

Font styles to use
Serif
Script

Requirements
Must have
• Warning label as written in description. Must be whimsical and attractive for a parent to purchase for their child

```html
<!DOCTYPE html>
<html lang="en">
<head>
<meta charset="utf-8">
<title>Plimmo Fizzles! Bubble Solution Label</title>
<link rel="stylesheet" href="https://fonts.googleapis.com/css2?family=Bowlby+One&family=Righteous&family=Audiowide&display=swap">
<style>
  :root {
    --ink: #000000;
    --paper: #ffffff;
    --bubble-light: #eef3ff;
    --bubble-sky: #b8cdf6;
    --bubble-violet: #a88ef0;
    --bubble-deep: #8f7ae8;
    --title: #14082e;
    --tagline: #1c6e00;
  }
  html, body {
    margin: 0;
    padding: 0;
    width: 1200px;
    height: 695px;
    overflow: hidden;
    background: var(--paper);
  }
  .label {
    position: relative;
    width: 1200px;
    height: 695px;
    overflow: hidden;
  }
  .bubble-field {
    position: absolute;
    inset: 0;
    background:
      radial-gradient(ellipse 55% 55% at 50% 45%, var(--bubble-deep) 0%, var(--bubble-violet) 35%, var(--bubble-sky) 70%, var(--bubble-light) 100%);
  }
  .artwork {
    position: absolute;
    inset: 0;
  }
  .brand-name {
    font-family: "Bowlby One", "Arial Black", sans-serif;
    font-size: 150px;
    fill: var(--title);
  }
  .tagline {
    font-family: "Righteous", "Arial Black", sans-serif;
    fill: var(--tagline);
  }
  .warning {
    position: absolute;
    left: 665px;
    top: 485px;
    width: 540px;
    margin: 0;
    text-align: center;
    font-family: "Audiowide", "Arial", sans-serif;
    font-size: 17px;
    line-height: 22px;
    color: var(--ink);
    text-transform: uppercase;
    letter-spacing: 0.5px;
  }
  .warning .maker {
    display: block;
  }
</style>
</head>
<body>
<main class="label">
  <div class="bubble-field" role="img" aria-label="Background of floating soap bubbles in blue and violet"></div>

  <svg class="artwork" width="1200" height="695" viewBox="0 0 1200 695" xmlns="http://www.w3.org/2000/svg">
    <text class="brand-name" x="600" y="215" text-anchor="middle" textLength="1120" lengthAdjust="spacingAndGlyphs">Plimmo Fizzles!</text>

    <g class="tagline">
      <text x="40" y="438" font-size="62" textLength="200" lengthAdjust="spacingAndGlyphs">LET'S</text>
      <text x="262" y="445" font-size="160" textLength="555" lengthAdjust="spacingAndGlyphs">FLOAT</text>
      <text x="842" y="420" font-size="72" textLength="325" lengthAdjust="spacingAndGlyphs">AND PLAY</text>
    </g>
  </svg>

  <p class="warning">
    Warning:"Do not drink bubble solution.<br>
    If swallowed drink lots of water.<br>
    Bubble solution is not intended<br>
    for human or animal consumption.<br>
    If it comes in contact with<br>
    your eyes, rinse immediately with water"
    <span class="maker">Sunnyloop LLC</span>
  </p>
</main>
</body>
</html>
```